Label Redesign For Hemp Oil Tincture Bottle*

I need a label redesigned for Meadowlark Botanics, current bottle label and logo is attached. The current label doesn't standout, not sure if its the font size or colors on the existing label. It is very important to have on the label that this is a Premium Full Spectrum Hemp Oil that is 2000mg. Then after the label is redesigned and approved, I would need to packaging to be designed to match the approved label design.
This Hemp oil has a relaxing effect to help ease mental and emotional stress, tension and worry. The Omega Fatty Acids it contains also naturally improves your mood and overall brain function, causing you to feel more alert and focused. Hemp Oil helps with insomnia. Take some 2-3 hours before bedtime, you will feel relaxed yet aware of how tired you are that it will lead to a good night's sleep. Hemp Oil helps ease chronic pain and inflammation from conditions such as arthritis, fibromyalgia, lupus, and MS. As a pain relief supplement, it is a safer, natural, non-chemical and non-addictive alternative to prescription painkillers.
Updates

Target Market(s)

Adults

Industry/Entity Type

Supplement

Font styles to use
Serif
Sans Serif

Colors

Designer to choose colors to be used in the design.

Requirements
Must have
• All information thats on current label but where it says 750 in the front of the existing label, it needs to say 2000. The 2000 should be prominent on the label.

```html
<!DOCTYPE html>
<html lang="en">
<head>
<meta charset="utf-8">
<title>Meadowlark Botanics – Premium Full Spectrum Hemp Oil 2000</title>
<link href="https://fonts.googleapis.com/css2?family=Archivo+Black&family=Arimo:wght@400;700&family=Oswald:wght@500&family=Tinos:wght@700&display=swap" rel="stylesheet">
<style>
  :root {
    --page-bg: #f2f2f2;
    --mint-light: #abeed8;
    --mint-mid: #94dcc3;
    --mint-deep: #7ab9a6;
    --ink: #333333;
    --paper: #ffffff;
    --leaf-green: #1fa653;
    --leaf-deep: #15803f;
  }
  * { margin: 0; padding: 0; box-sizing: border-box; }
  html, body {
    width: 755px;
    height: 1200px;
    overflow: hidden;
    background: var(--page-bg);
  }
  .canvas {
    position: relative;
    width: 755px;
    height: 1200px;
  }
  .label {
    position: absolute;
    left: 50px;
    top: 185px;
    width: 655px;
    height: 830px;
    background: linear-gradient(90deg, var(--mint-light) 0%, var(--mint-mid) 55%, var(--mint-deep) 100%);
    overflow: hidden;
    color: var(--ink);
  }
  .thc-claim {
    position: absolute;
    left: 38px;
    top: 38px;
    font-family: "Tinos", serif;
    font-weight: 700;
    font-size: 27px;
  }
  .net-content {
    position: absolute;
    right: 30px;
    top: 24px;
    text-align: right;
    font-family: "Arimo", sans-serif;
    font-weight: 700;
    font-size: 23px;
    line-height: 1.25;
  }
  .brand-pennant {
    position: absolute;
    left: 257px;
    top: 0;
    width: 140px;
    height: 180px;
  }
  .brand-pennant svg { position: absolute; inset: 0; }
  .brand-mark {
    position: absolute;
    left: 0;
    right: 0;
    top: 58px;
    text-align: center;
    font-family: "Arimo", sans-serif;
    font-weight: 700;
    font-size: 14px;
    line-height: 1.25;
    color: var(--ink);
  }
  .product-title {
    position: absolute;
    left: 0;
    right: 0;
    top: 210px;
    text-align: center;
    font-family: "Archivo Black", sans-serif;
    font-size: 52px;
    line-height: 56px;
    letter-spacing: 1px;
  }
  .strength {
    position: absolute;
    left: 0;
    right: 0;
    top: 376px;
    text-align: center;
    font-family: "Oswald", sans-serif;
    font-weight: 500;
    font-size: 124px;
    line-height: 124px;
    letter-spacing: -2px;
  }
  .brand-plate {
    position: absolute;
    left: 92px;
    top: 498px;
    width: 470px;
    height: 76px;
    background: var(--paper);
    display: flex;
    align-items: center;
    justify-content: center;
    text-align: center;
    white-space: nowrap;
    font-family: "Arimo", sans-serif;
    font-weight: 700;
    font-size: 31px;
  }
  .supplement-line {
    position: absolute;
    left: 0;
    right: 0;
    top: 592px;
    text-align: center;
    font-family: "Arimo", sans-serif;
    font-size: 27px;
  }
  .flavor-line {
    position: absolute;
    left: 0;
    right: 0;
    top: 630px;
    text-align: center;
    font-family: "Arimo", sans-serif;
    font-size: 21px;
  }
  .leaf-band {
    position: absolute;
    left: 0;
    right: 0;
    bottom: 0;
    height: 150px;
    background: linear-gradient(180deg, rgba(31,166,83,0) 0%, var(--leaf-green) 45%, var(--leaf-deep) 100%);
  }
</style>
</head>
<body>
  <main class="canvas">
    <section class="label">
      <div class="thc-claim">Zero THC</div>
      <div class="net-content">2000 mg<br>1fl.oz (30ml)</div>

      <div class="brand-pennant">
        <svg width="140" height="180" viewBox="0 0 140 180" aria-hidden="true">
          <polygon points="0,0 140,0 140,145 70,180 0,145" fill="#ffffff"/>
        </svg>
        <div class="brand-mark">Meadowlark<br>Botanics</div>
      </div>

      <h1 class="product-title">PREMIUM<br>FULL SPECTRUM<br>HEMP OIL</h1>
      <div class="strength">2000</div>

      <div class="brand-plate">MEADOWLARK BOTANICS</div>

      <div class="supplement-line">DIETARY SUPPLIMENT</div>
      <div class="flavor-line">NATURAL PEPPERMINT FLAVOR</div>

      <div class="leaf-band" role="img" aria-label="Illustration of green hemp leaves along the bottom of the label"></div>
    </section>
  </main>
</body>
</html>
```